Business Card Design

I'm a young beekeeper (22 years old) just starting out. I own and run 80 hives and would like to eventually build up to 1000. My aim is to run it in tandem with our family farm that is currently running sheep and beef. Unlike a number of honey companies on the East Coast (or the North Island, NZ) I am local and will expand onto the lease blocks that our family is also leasing. I want a simple plain logo/photo. The designer may wish to use one of the photos as a background outline or however they chose. The mountain is Aorangi and our farm borders one side of it.

Target Market(s)

From local land owners to wholesale honey buyers

Industry/Entity Type

Farm

Contact Information for Business Card

Pekeriu Honey
Manager Owner Manaia Brooks
email pekeriuhoney@tuimailbox.co.nz
mobile 0217394461

Requirements
Must have
• The details submitted. The brand Pekeriu Honey to be the main feature. The other details can be smaller.
Should not have
• Must not include a picture of a bee or hive. Use a modern font. Don't use koru but may incorporate poutama.

```html
<!DOCTYPE html>
<html lang="en">
<head>
<meta charset="utf-8">
<title>Pekeriu Honey – Business Card</title>
<link rel="stylesheet" href="https://fonts.googleapis.com/css2?family=Arimo:wght@400&family=Great+Vibes&display=swap">
<style>
  :root {
    --page-bg: #e9e9e7;
    --ink: #111111;
    --brand: #ffffff;
    --sky-top: #7fb6e2;
    --sky-haze: #e4f0f8;
    --ridge: #4b5967;
    --bush: #2e3b38;
    --grass-light: #9a8757;
    --grass-dark: #5b5033;
    --card-shadow: rgba(0, 0, 0, 0.25);
  }
  html, body {
    margin: 0;
    width: 1200px;
    height: 900px;
    overflow: hidden;
    background: var(--page-bg);
  }
  .card {
    position: absolute;
    left: 100px;
    top: 164px;
    width: 1000px;
    height: 572px;
    overflow: hidden;
    box-shadow: 0 10px 30px var(--card-shadow);
  }
  .card__landscape {
    position: absolute;
    inset: 0;
    background: linear-gradient(
      to bottom,
      var(--sky-top) 0%,
      var(--sky-haze) 30%,
      #c9d7e2 38%,
      var(--ridge) 46%,
      var(--bush) 68%,
      var(--grass-light) 82%,
      var(--grass-dark) 100%
    );
  }
  .card__person {
    position: absolute;
    left: 56px;
    top: 140px;
    margin: 0;
    font-family: "Arimo", Arial, sans-serif;
    font-size: 22px;
    line-height: 1.15;
    color: var(--ink);
  }
  .card__person-name {
    display: block;
    text-transform: uppercase;
    letter-spacing: 0.5px;
  }
  .card__contact {
    position: absolute;
    right: 34px;
    top: 34px;
    margin: 0;
    padding: 0;
    list-style: none;
    font-family: "Arimo", Arial, sans-serif;
    font-size: 20px;
    line-height: 1.35;
    color: var(--ink);
    text-align: right;
  }
  .card__contact-item {
    display: flex;
    justify-content: flex-end;
    align-items: center;
    gap: 8px;
  }
  .card__icon {
    width: 20px;
    height: 18px;
    flex: none;
  }
  .card__brand {
    position: absolute;
    left: 330px;
    top: 300px;
    margin: 0;
    font-family: "Great Vibes", cursive;
    font-weight: 400;
    font-size: 112px;
    line-height: 1;
    color: var(--brand);
    white-space: nowrap;
  }
</style>
</head>
<body>
  <article class="card">
    <div class="card__landscape" role="img" aria-label="Photograph of a mountain under a blue sky, with bush-covered slopes and golden grassland in the foreground"></div>

    <p class="card__person">
      <span class="card__person-name">Manaia Brooks</span>
      Manager<br>
      Owner
    </p>

    <ul class="card__contact">
      <li class="card__contact-item">
        <span>pekeriuhoney@tuimailbox.co.nz</span>
        <svg class="card__icon" viewBox="0 0 20 18" aria-hidden="true">
          <rect x="1" y="3" width="18" height="12" fill="var(--ink)"/>
          <path d="M1 3 L10 10 L19 3" fill="none" stroke="#ffffff" stroke-width="1.4"/>
        </svg>
      </li>
      <li class="card__contact-item">
        <span>0217394461</span>
        <svg class="card__icon" viewBox="0 0 20 18" aria-hidden="true">
          <rect x="1" y="0" width="18" height="18" rx="2" fill="var(--ink)"/>
          <path d="M6 4 C5 5 5 7 7 10 C9 13 11 14 13 14 L14.5 12.5 L12 10.5 L11 11.5 C10 11 8.5 9.5 8 8.5 L9 7.5 L7.5 4.5 Z" fill="#ffffff"/>
        </svg>
      </li>
    </ul>

    <h1 class="card__brand">Pekeriu Honey</h1>
  </article>
</body>
</html>
```